Skincare Cleanser Bottle Label

New product launch of a mint facial cleanser.
Brand is called Dorvella.
Product will be called Lumora.
Looking for a label design that can be printed using silk screening.
High gloss white plastic bottle. 8oz. White push pump top.
Clinical skincare brand, professional image, sold in medical spas.

Target Market(s)

Women Age 20-65

Industry/Entity Type

Health And Wellness

Font styles to use
Serif
Sans Serif

Requirements
Must have
• Dorvella brand name in the orignal font.
Should not have
• Multiple colours.

```html
<!DOCTYPE html>
<html lang="en">
<head>
<meta charset="utf-8">
<title>Dorvella Lumora Label</title>
<link href="https://fonts.googleapis.com/css2?family=Montserrat:wght@400;700&display=swap" rel="stylesheet">
<style>
  :root {
    --page-bg: #e6e6e6;
    --label-bg: #ffffff;
    --ink: #2f2f2f;
    --ink-soft: #6d6d6d;
    --leaf-light: #e4e4e4;
    --leaf-dark: #8a8a8a;
  }
  html, body {
    margin: 0;
    width: 1200px;
    height: 1200px;
    overflow: hidden;
    background: var(--page-bg);
  }
  .label {
    position: absolute;
    left: 334px;
    top: 107px;
    width: 532px;
    height: 985px;
    background: var(--label-bg);
  }
  .brand-name {
    position: absolute;
    left: -260px;
    top: 423px;
    width: 665px;
    height: 90px;
    line-height: 90px;
    text-align: center;
    transform: rotate(-90deg);
    font-family: "Montserrat", sans-serif;
    font-weight: 400;
    font-size: 72px;
    letter-spacing: 6px;
    color: var(--ink);
    white-space: nowrap;
  }
  .leaf-art {
    position: absolute;
    left: 174px;
    top: 204px;
    width: 217px;
    height: 244px;
    border-radius: 40% 40% 30% 30%;
    background: radial-gradient(circle at 40% 35%, var(--leaf-light), var(--leaf-dark));
  }
  .product-name {
    position: absolute;
    left: 172px;
    top: 550px;
    margin: 0;
    font-family: "Montserrat", sans-serif;
    font-weight: 700;
    font-size: 44px;
    letter-spacing: 1px;
    color: var(--ink);
  }
  .product-type {
    position: absolute;
    left: 174px;
    top: 606px;
    margin: 0;
    font-family: "Montserrat", sans-serif;
    font-weight: 400;
    font-size: 24px;
    color: var(--ink-soft);
  }
  .volume {
    position: absolute;
    left: 323px;
    top: 702px;
    margin: 0;
    font-family: "Montserrat", sans-serif;
    font-weight: 400;
    font-size: 22px;
    color: var(--ink);
  }
</style>
</head>
<body>
  <main class="label">
    <div class="brand-name">DORVELLA</div>
    <div class="leaf-art" role="img" aria-label="Illustration of three grey mint leaves"></div>
    <h1 class="product-name">LUMORA</h1>
    <p class="product-type">Mint Facial Wash</p>
    <p class="volume">8 fl. Oz.</p>
  </main>
</body>
</html>
```